New CD - "Tunes About Marla" (Jazz piano standards)

We need a CD design for album of jazz piano standards. The music is elegant, fun, and artistic. Appeals to all lovers of Halvorsen, Brenton, Dubrow, etc. Includes Red Harbor, Can't Stop Dancin', Harbor Serenade, She Keeps A Secret In Her Pocket, Rain Falls On Quiet Streets, Lazy Tuesday, (Tonight) Across The Meadow, Hours by Candle and Lace, When Rivers Bend, Only If You Call, Your Quiet Spark, She Always Left The Door, Remarkable Dawn, Nocturne Op. 41, No. 7 "Lamplight"/T. Varga.

Target Market(s)

Anyone who likes piano music.

```html
<!DOCTYPE html>
<html lang="en">
<head>
<meta charset="utf-8">
<title>Tunes About Marla</title>
<link href="https://fonts.googleapis.com/css2?family=Yanone+Kaffeesatz:wght@300;400&family=Zilla+Slab:wght@300;400&display=swap" rel="stylesheet">
<style>
  :root {
    --bg-dark: #1c1c1c;
    --bg-mid: #3a3a3a;
    --text-light: #f2f2f2;
    --text-soft: #d9d9d9;
    --gold: #f0b231;
    --photo-tone: #3b3430;
  }
  * { margin: 0; padding: 0; box-sizing: border-box; }
  html, body { width: 1200px; height: 1200px; overflow: hidden; background: var(--bg-dark); }
  .cover {
    position: relative;
    width: 1200px;
    height: 1200px;
    overflow: hidden;
    background: radial-gradient(ellipse at 50% 20%, var(--bg-mid) 0%, #2a2a2a 45%, var(--bg-dark) 100%);
  }
  .cover-shapes { position: absolute; inset: 0; }
  .tracklist {
    position: absolute;
    left: 55px;
    top: 104px;
    list-style: none;
    font-family: "Yanone Kaffeesatz", sans-serif;
    font-weight: 300;
    font-size: 37px;
    line-height: 42.5px;
    color: var(--text-light);
    letter-spacing: 0.2px;
    white-space: nowrap;
  }
  .tracklist .num { display: inline-block; width: 44px; }
  .artist-photo {
    position: absolute;
    left: 760px;
    top: 300px;
    width: 440px;
    height: 820px;
    border-radius: 200px 200px 0 0;
    background: linear-gradient(180deg, #8a6a55 0%, var(--photo-tone) 38%, #1f2228 100%);
  }
  .album-title {
    position: absolute;
    left: 55px;
    top: 770px;
    font-family: "Zilla Slab", serif;
    font-weight: 300;
    line-height: 1;
  }
  .album-title .lead {
    display: block;
    font-size: 112px;
    color: var(--text-light);
  }
  .album-title .name {
    display: block;
    margin-top: -30px;
    margin-left: -6px;
    font-size: 252px;
    color: var(--gold);
    letter-spacing: 2px;
  }
  .copyright {
    position: absolute;
    left: 56px;
    top: 1124px;
    font-family: "Zilla Slab", serif;
    font-weight: 300;
    font-size: 26px;
    color: var(--text-soft);
    word-spacing: 3px;
    white-space: nowrap;
  }
</style>
</head>
<body>
<main class="cover">
  <svg class="cover-shapes" width="1200" height="1200" viewBox="0 0 1200 1200" aria-hidden="true">
    <polygon points="0,960 1200,1060 1200,1200 0,1200" fill="#161616" opacity="0.55"/>
  </svg>

  <div class="artist-photo" role="img" aria-label="Portrait of the pianist in a dark suit and blue tie"></div>

  <svg class="cover-shapes" width="1200" height="1200" viewBox="0 0 1200 1200" aria-hidden="true">
    <polygon points="1200,735 1200,1200 1088,1200" fill="var(--gold)"/>
  </svg>

  <ol class="tracklist">
    <li><span class="num">1.</span>She Keeps A Secret In Her Pocket/H. Corwin (2:22)</li>
    <li><span class="num">2.</span>Rain Falls On Quiet Streets/J. Lathrop &amp; O. Pellman (3:29)</li>
    <li><span class="num">3.</span>Red Harbor/R. Brenton (3:31)</li>
    <li><span class="num">4.</span>Lazy Tuesday/H. Corwin (2:08)</li>
    <li><span class="num">5.</span>Across The Meadow/H. Corwin &amp; E.Y. Stanwick (4:12)</li>
    <li><span class="num">6.</span>Hours by Candle and Lace/H. Dubrow &amp; J. Follett (2:54)</li>
    <li><span class="num">7.</span>When Rivers Bend/H. Brandvik (1:51)</li>
    <li><span class="num">8.</span>Can't Stop Dancin'/F. Delmore (2:15)</li>
    <li><span class="num">9.</span>Only If You Call/G. Halvorsen (4:17)</li>
    <li><span class="num">10.</span>Harbor Serenade/K. Ashby &amp; J. Terrano (2:21)</li>
    <li><span class="num">11.</span>Your Quiet Spark/V. Ostrand (3:34)</li>
    <li><span class="num">12.</span>She Always Left The Door/R. Brenton (2:49)</li>
    <li><span class="num">13.</span>Remarkable Dawn/G. Halvorsen (2:13)</li>
    <li><span class="num">14.</span>Nocturne Op. 41, No. 7 "Lamplight"/T. Varga (5:46)</li>
  </ol>

  <h1 class="album-title">
    <span class="lead">Tunes About</span>
    <span class="name">Marla</span>
  </h1>

  <p class="copyright">Copyright © 2016 Frederick Ellison&nbsp;&nbsp;All Rights Reserved</p>
</main>
</body>
</html>
```